New Fun, Positive, energised looking Business Card Needed for High Achiever Coach

I am looking for a two sided full colour business card. I am self employed and have recently re branded my 1-2-1 work re-vitalising high achievers. My target client base for these cards is therefore high achievers - usually aged 40 -55, they are often entrepreneurs, CEO or work in banking and finance and 2/3 are male. I work with them on 90 day or 6 month coaching programs to help them live their success in a healthier, more sustainable and fulfiiled way. They pay for this privately so though they are corporate types the cards need not look 'corporate'. I want to portray the idea of transformation, vitality and re-connecting.
You can get a feel for the look I like on my new website: corinvale.co.uk
I want to use this logo with strapline (Re-Vitalising High Achievers) (I purchased off Logoharbor) and font/ colours (the turquoise and green).
Details to include on the card:
www.corinvale.co.uk
+44 7915 264318
mira@corinvale.co.uk
skype: miracorin
I'd also like to include:
Do you struggle to switch off? Want to be healthier and feel fitter? Want closer relationships? More clarity over the direction you are headed? I can help you do these things using integrated mind-body techniques. Visit corinvale.co.uk TODAY to apply for a FREE Breakthrough session.
BUT if that is too much text for a card I am open to advice/ammendments.
Updates
Thanks for your design - I am considering them. PLease change the wording to :

```html
<!DOCTYPE html>
<html lang="en">
<head>
<meta charset="utf-8">
<title>Mira Corinvale – Business Card</title>
<link rel="stylesheet" href="https://fonts.googleapis.com/css2?family=Open+Sans:wght@400;600;700&display=swap">
<style>
  :root {
    --turquoise: #1a9fc4;
    --green: #4db561;
    --ink: #4a4a4a;
    --rule: #c9c9c9;
    --card: #ffffff;
    --backdrop: #ececec;
  }
  * { box-sizing: border-box; margin: 0; padding: 0; }
  html, body {
    width: 1200px; height: 720px; overflow: hidden;
    background: var(--backdrop);
    font-family: "Open Sans", Arial, sans-serif;
    color: var(--ink);
  }
  .canvas { position: relative; width: 1200px; height: 720px; }
  .card {
    position: absolute; top: 205px;
    width: 540px; height: 310px;
    background: var(--card);
    box-shadow: 0 4px 14px rgba(0,0,0,0.12);
    overflow: hidden;
  }
  .card--front { left: 40px; }
  .card--back { left: 620px; }

  .brand {
    position: absolute; display: flex; flex-direction: column; align-items: center;
  }
  .brand__mark {
    width: 54px; height: 54px; border-radius: 50%;
    background: var(--green); margin-bottom: 12px;
  }
  .brand__name {
    font-weight: 700; color: var(--turquoise); white-space: nowrap;
  }
  .brand__tagline {
    color: var(--turquoise); font-weight: 400; white-space: nowrap;
  }
  .card--front .brand { left: 40px; top: 62px; width: 200px; }
  .card--front .brand__name { font-size: 21px; }
  .card--front .brand__tagline { font-size: 11px; }

  .divider {
    position: absolute; width: 1px; background: var(--rule);
  }
  .card--front .divider { left: 262px; top: 36px; height: 120px; transform: rotate(-8deg); }

  .contact-list {
    position: absolute; left: 282px; top: 44px; list-style: none;
    font-size: 13.5px;
  }
  .contact-list li { display: flex; align-items: center; gap: 8px; margin-bottom: 10px; }
  .contact-list svg { width: 14px; height: 14px; flex: none; }

  .bands { position: absolute; left: 0; top: 0; width: 540px; height: 310px; }
  .web-address {
    position: absolute; right: 24px; top: 193px;
    color: #fff; font-weight: 600; font-size: 15px; letter-spacing: 1.5px;
  }

  .card--back .brand { left: 30px; top: 90px; width: 210px; }
  .card--back .brand__name { font-size: 22px; }
  .card--back .brand__tagline { font-size: 11.5px; }
  .card--back .divider { left: 250px; top: 20px; height: 270px; }

  .pitch {
    position: absolute; left: 268px; top: 44px; width: 252px;
    font-size: 12.5px; line-height: 1.55;
  }
  .pitch p + p { margin-top: 12px; }
  .pitch strong { font-weight: 700; }
</style>
</head>
<body>
<main class="canvas">

  <section class="card card--front" aria-label="Business card front">
    <svg class="bands" viewBox="0 0 540 310" aria-hidden="true">
      <polygon points="0,272 300,244 300,256 0,284" fill="var(--green)"/>
      <polygon points="292,192 540,182 540,212 272,222" fill="var(--turquoise)"/>
    </svg>

    <div class="brand">
      <span class="brand__mark"></span>
      <span class="brand__name">Mira Corinvale</span>
      <span class="brand__tagline">Re-Vitalising High Achievers</span>
    </div>

    <span class="divider"></span>

    <ul class="contact-list">
      <li>
        <svg viewBox="0 0 16 16"><circle cx="8" cy="8" r="7.5" fill="var(--turquoise)"/><path d="M5.4 4.2l1.3 1.9-.8.9c.5 1.2 1.4 2.1 2.6 2.6l.9-.8 1.9 1.3-.6 1.5c-3.3-.3-5.9-2.9-6.2-6.2z" fill="#fff"/></svg>
        <span>+44 7915 264318</span>
      </li>
      <li>
        <svg viewBox="0 0 16 16"><circle cx="8" cy="8" r="7.5" fill="var(--turquoise)"/><rect x="4" y="5" width="8" height="6" fill="#fff"/><path d="M4 5l4 3.3L12 5" stroke="var(--turquoise)" stroke-width="1" fill="none"/></svg>
        <span>mira@corinvale.co.uk</span>
      </li>
      <li>
        <svg viewBox="0 0 16 16"><rect x="1" y="1" width="14" height="14" rx="2" fill="var(--turquoise)"/></svg>
        <span>miracorin</span>
      </li>
    </ul>

    <span class="web-address">www.corinvale.co.uk</span>
  </section>

  <section class="card card--back" aria-label="Business card back">
    <div class="brand">
      <span class="brand__mark"></span>
      <span class="brand__name">Mira Corinvale</span>
      <span class="brand__tagline">Re-Vitalising High Achievers</span>
    </div>

    <span class="divider"></span>

    <div class="pitch">
      <p>Do you struggle to switch off?<br>
      Want to be healthier and feel fitter?<br>
      Want closer relationships?<br>
      More clarity over the direction you are headed?</p>
      <p>I can help you do these things using integrated mind-body techniques.</p>
      <p>Visit <strong>corinvale.co.uk</strong> TODAY to apply for a FREE Breakthrough session.</p>
    </div>
  </section>

</main>
</body>
</html>
```